Velmoxa AdAgency Presentation

We need ppt design for an ad agency re-branding, agency is based in Moscow, Russia. Our specifics is brand audit, consulting and strategy in web and offline.
We decided to do re-branding because our current agency does not answer the purpose and we need a kind of "second breath".
The idea of re-branding appeared because of many changes that happened in company: new clients, new projects level, new team.
So we'd like to promote company of changes and design should show this spirit as possible.
You may use info in attached pdf file (sorry for Russian language). Info is not so necessary, it will be replaced later.

Please use more colors than digital blue and grey!

Industry/Entity Type

Ad Agency

Requirements
Must have
• Logo is attached. Please choose one.

Ppt project should include:
- Front and last page design
- Heading and list design
- Page-separator design
- Diagram design
- Pics appearance

```html
<!DOCTYPE html>
<html lang="en">
<head>
<meta charset="utf-8">
<title>Velmoxa Agency Presentation</title>
<link rel="stylesheet" href="https://fonts.googleapis.com/css2?family=Montserrat:wght@400;700&family=Open+Sans:wght@400;600;700&display=swap">
<style>
:root{
  --page:#000;
  --paper:#fff;
  --paper-soft:#eef2f5;
  --blue:#2d8fd2;
  --blue-deep:#1b6aa8;
  --sky:#6cc0ea;
  --map:#4aa6dd;
  --ink:#1f2328;
  --text:#555b62;
  --row:#e6eef4;
  --pink:#e8457f;
  --yellow:#f6d23a;
  --green:#7cc94e;
  --violet:#8a5bd1;
  --orange:#f39a3b;
}
*{margin:0;padding:0;box-sizing:border-box}
html,body{width:814px;height:1200px;overflow:hidden;background:var(--page)}
body{font-family:"Open Sans",Arial,sans-serif;color:var(--text)}
.sheet{position:relative;width:814px;height:1200px}
.slide{position:absolute;width:256px;height:192px;background:var(--paper);overflow:hidden}
.c1{left:8px}.c2{left:279px}.c3{left:550px}
.r1{top:3px}.r2{top:203px}.r3{top:403px}.r4{top:603px}.r5{top:803px}.r6{top:1003px}

.title{position:absolute;left:12px;top:16px;font-family:"Montserrat",sans-serif;font-weight:700;font-size:6.6px;color:var(--ink);letter-spacing:.1px}
.brand{position:absolute;right:9px;top:6px;display:flex;flex-direction:column;align-items:center;gap:1px;font-family:"Montserrat",sans-serif;font-size:4px;color:var(--blue)}
.brand i{display:block;width:7px;height:7px;background:var(--blue)}
.footer{position:absolute;left:0;right:0;bottom:0;height:15px;background:linear-gradient(90deg,var(--blue-deep),var(--blue) 60%,var(--sky))}
.footer::before{content:"";position:absolute;left:0;right:0;top:-3px;height:3px;background:var(--sky);opacity:.6}
.cubes{position:absolute;left:0;bottom:0;height:15px;width:70px;background:linear-gradient(90deg,var(--pink),var(--yellow) 30%,var(--green) 55%,var(--violet) 80%,rgba(45,143,210,0))}
.copy{position:absolute;left:80px;bottom:5px;font-size:3.2px;color:#dbeefa}
.num{position:absolute;right:10px;bottom:5px;font-size:3.2px;color:#dbeefa}

p.body{font-size:3.6px;line-height:1.45;color:var(--text);text-align:justify}
p.body+p.body{margin-top:3px}
.photo{position:absolute;border-radius:1px}

.cover{background:linear-gradient(170deg,var(--sky),var(--blue) 55%,var(--blue-deep))}
.cover .mark{position:absolute;left:24px;top:52px;display:flex;flex-direction:column;gap:4px;color:#fff;font-family:"Montserrat",sans-serif;font-size:10px}
.cover .mark i{display:block;width:24px;height:24px;background:#fff}
.cube-field{position:absolute;left:0;right:0;bottom:0;height:62px;background:linear-gradient(100deg,var(--pink),var(--orange) 22%,var(--yellow) 40%,var(--green) 60%,var(--violet) 80%,var(--pink))}
.hero{background:var(--paper-soft)}
.hero .band{position:absolute;left:0;right:0;top:56px;height:68px;background:linear-gradient(180deg,#fff,#e3eef6)}
.hero .big{position:absolute;left:0;right:0;top:78px;text-align:center;font-family:"Montserrat",sans-serif;font-weight:700;font-size:15px;color:var(--blue)}
.hero .sub{position:absolute;left:0;right:0;top:97px;text-align:center;font-size:4.5px;color:var(--sky);letter-spacing:.5px}
.hero .brand-lg{position:absolute;right:16px;top:16px;display:flex;flex-direction:column;align-items:center;gap:2px;font-family:"Montserrat",sans-serif;font-size:6px;color:var(--blue)}
.hero .brand-lg i{display:block;width:14px;height:14px;background:var(--blue)}
.hero .strip{position:absolute;left:0;right:0;bottom:0;height:62px;background:linear-gradient(180deg,var(--sky),var(--blue-deep))}
.divider .band{background:linear-gradient(180deg,var(--sky),var(--blue))}
.divider .big{color:#fff;text-align:left;left:14px;top:76px}
.divider .sub{color:#d9f0fb;text-align:left;left:14px}
.divider .strip{height:58px;background:linear-gradient(100deg,var(--pink),var(--orange) 25%,var(--yellow) 45%,var(--green) 65%,var(--violet) 85%,var(--pink))}
.divider .fcopy{position:absolute;left:80px;bottom:62px;font-size:3.2px;color:var(--blue)}
.closing .strip{height:112px}
.closing .band{top:40px;height:40px}

.item{position:absolute;display:flex;gap:5px;align-items:flex-start}
.dot{flex:none;width:9px;height:9px;border-radius:50%;background:var(--blue);color:#fff;font-size:4px;font-weight:700;display:flex;align-items:center;justify-content:center}
.item h4{font-size:4px;font-weight:700;color:var(--ink);margin-bottom:1px}
.item p{font-size:3.3px;line-height:1.4}

.device{position:absolute;background:linear-gradient(160deg,#3a4350,#8a6b5a 50%,#c7533f);border:1.5px solid #2a2f36;border-radius:1px}
.device::after{content:"";position:absolute;left:-5px;right:-5px;bottom:-4px;height:2px;background:#9aa3ab;border-radius:1px}
.cap{position:absolute;font-size:3.3px;line-height:1.4;text-align:center}
.cap b{display:block;color:var(--ink);font-size:3.6px}

.map-area{position:absolute;left:34px;top:40px;width:196px;height:102px;border-radius:4px;background:linear-gradient(180deg,#7cc1e8,var(--map))}

table.data{position:absolute;border-collapse:collapse;font-size:3.3px}
table.data th{background:var(--blue);color:#fff;font-weight:600;padding:2px 3px;text-align:left}
table.data td{padding:1.6px 3px;color:var(--text)}
table.data tr:nth-child(even) td{background:var(--row)}

.bullets{position:absolute;list-style:none;font-size:3.4px;line-height:2.1}
.bullets li::before{content:"";display:inline-block;width:2.5px;height:2.5px;background:var(--blue);margin-right:4px;vertical-align:middle}
.legend{position:absolute;font-size:3px;display:flex;gap:7px;color:var(--text)}
</style>
</head>
<body>
<main class="sheet">

<section class="slide cover c1 r1">
  <div class="mark"><i></i>Velmoxa</div>
  <div class="cube-field" role="img" aria-label="Field of bright multicoloured tumbling cubes"></div>
  <span class="copy" style="top:6px;left:10px;bottom:auto">© 2013 Velmoxa. All rights reserved</span>
</section>

<section class="slide hero c2 r1">
  <div class="brand-lg"><i></i>Velmoxa</div>
  <div class="band"></div>
  <div class="big">YOUR TITTLE HERE</div>
  <div class="sub">YOUR PRESENTATION SUB TITLE HERE</div>
  <div class="strip" role="img" aria-label="Soft blue city skyline backdrop"></div>
  <span class="copy" style="left:auto;right:10px">© 2013 Velmoxa. All rights reserved</span>
</section>

<section class="slide c3 r1">
  <h2 class="title">VELMOXA PRESENTATION POWERFUL MISSION 1</h2>
  <div class="brand"><i></i>Velmoxa</div>
  <div class="photo" style="left:22px;top:40px;width:62px;height:70px;background:linear-gradient(180deg,#2a3b5a,#5a6f8f 55%,#d9a860)" role="img" aria-label="Lit office tower at dusk"></div>
  <div style="position:absolute;left:100px;top:44px;width:140px">
    <p class="body">The agency has forged a courageous and dynamic approach to the methods of brand research. By overcoming old habits that held the field back, the team has raised the level of strategy to a new standard.</p>
    <p class="body">Central to this approach are focused audits that hold the work together. The team has raised the bar of multiple projects and clients to a new level and keeps the spirit of change in every task.</p>
  </div>
  <div class="footer"><div class="cubes"></div><span class="copy">© 2013 Velmoxa. All rights reserved</span><span class="num">3</span></div>
</section>

<section class="slide c1 r2">
  <h2 class="title">VELMOXA PRESENTATION POWERFUL MISSION 1</h2>
  <div class="brand"><i></i>Velmoxa</div>
  <div class="item" style="left:26px;top:42px;width:200px"><span class="dot">1</span><div><h4>We know first hand 1</h4><p>Since 1990, we have supported thousands of clients from the point of first brief through their journey with the agency.</p></div></div>
  <div class="item" style="left:26px;top:72px;width:200px"><span class="dot">2</span><div><h4>We know first hand 2</h4><p>Since 1990, we have supported thousands of clients from the point of first brief through their journey with the agency, we have supported thousands of clients from the point of brief.</p></div></div>
  <div class="item" style="left:26px;top:106px;width:200px"><span class="dot">3</span><div><h4>We know first hand 3</h4><p>Since 1990, we have supported thousands of clients, we have supported thousands of projects.</p></div></div>
  <div class="footer"><div class="cubes"></div><span class="copy">© 2013 Velmoxa. All rights reserved</span><span class="num">4</span></div>
</section>

<section class="slide c2 r2">
  <h2 class="title">VELMOXA PRESENTATION POWERFUL MISSION 1</h2>
  <div class="brand"><i></i>Velmoxa</div>
  <div class="item" style="left:22px;top:38px;width:100px"><span class="dot">1</span><div><h4>We know first hand 1</h4><p>Since 1990, we have supported thousands of clients from the first brief through their journey.</p></div></div>
  <div class="item" style="left:22px;top:72px;width:100px"><span class="dot">2</span><div><h4>We know first hand 2</h4><p>Since 1990, we have supported thousands of clients from the first brief.</p></div></div>
  <div class="item" style="left:22px;top:104px;width:100px"><span class="dot">3</span><div><h4>We know first hand 3</h4><p>Since 1990, we have supported thousands of clients from the first brief through their journey.</p></div></div>
  <div class="item" style="left:134px;top:38px;width:100px"><span class="dot">4</span><div><h4>We know first hand 4</h4><p>Since 1990, we have supported thousands of clients from the first brief through their journey.</p></div></div>
  <div class="item" style="left:134px;top:72px;width:100px"><span class="dot">5</span><div><h4>We know first hand 5</h4><p>Since 1990, we have supported thousands of clients from the first brief.</p></div></div>
  <div class="item" style="left:134px;top:104px;width:100px"><span class="dot">6</span><div><h4>We know first hand 6</h4><p>Since 1990, we have supported thousands of clients from the first brief.</p></div></div>
  <div class="footer"><div class="cubes"></div><span class="copy">© 2013 Velmoxa. All rights reserved</span><span class="num">5</span></div>
</section>

<section class="slide c3 r2">
  <h2 class="title">VELMOXA PRESENTATION POWERFUL MISSION 1</h2>
  <div class="brand"><i></i>Velmoxa</div>
  <div class="device" style="left:36px;top:46px;width:44px;height:28px" role="img" aria-label="Laptop showing a campaign image"></div>
  <div class="device" style="left:106px;top:46px;width:44px;height:28px" role="img" aria-label="Laptop showing a campaign image"></div>
  <div class="device" style="left:176px;top:46px;width:44px;height:28px" role="img" aria-label="Laptop showing a campaign image"></div>
  <div class="cap" style="left:26px;top:86px;width:64px"><b>Full Sale in Greenwich</b>Mostly recent work cases included from the team and partners across our markets.</div>
  <div class="cap" style="left:96px;top:86px;width:64px"><b>Full Sale in Greenwich</b>Mostly recent work cases included from the team and partners.</div>
  <div class="cap" style="left:166px;top:86px;width:64px"><b>Full Sale in Greenwich</b>Mostly recent work cases included from the team and partners.</div>
  <div class="footer"><div class="cubes"></div><span class="copy">© 2013 Velmoxa. All rights reserved</span><span class="num">6</span></div>
</section>

<section class="slide c1 r3">
  <h2 class="title">VELMOXA PRESENTATION POWERFUL MISSION 1</h2>
  <div class="brand"><i></i>Velmoxa</div>
  <div class="photo" style="left:18px;top:52px;width:100px;height:58px;background:linear-gradient(135deg,#e7e9eb,#d9724a 40%,#5a3a34 75%)" role="img" aria-label="Laptop, tablet and phone showing campaign visuals"></div>
  <div style="position:absolute;left:128px;top:40px;width:112px">
    <p class="body">The agency has forged a courageous and dynamic approach to the methods of brand research. By overcoming old habits that held the field back, the team has raised the level of strategy.</p>
    <p class="body">Central to this approach are focused audits that hold the work together. The team raised the bar for many projects and keeps the spirit of change.</p>
  </div>
  <div class="footer"><div class="cubes"></div><span class="copy">© 2013 Velmoxa. All rights reserved</span><span class="num">7</span></div>
</section>

<section class="slide c2 r3">
  <h2 class="title">VELMOXA PRESENTATION POWERFUL MISSION 1</h2>
  <div class="brand"><i></i>Velmoxa</div>
  <div class="device" style="left:40px;top:40px;width:30px;height:19px" role="img" aria-label="Laptop showing a campaign image"></div>
  <div class="cap" style="left:80px;top:38px;width:110px;text-align:left"><b>Full Sale in Greenwich</b>Mostly recent work cases included from the team and partners across our markets and clients.</div>
  <div class="device" style="left:40px;top:74px;width:30px;height:19px" role="img" aria-label="Laptop showing a campaign image"></div>
  <div class="cap" style="left:80px;top:72px;width:110px;text-align:left"><b>Full Sale in Greenwich</b>Mostly recent work cases included from the team and partners.</div>
  <div class="device" style="left:40px;top:108px;width:30px;height:19px" role="img" aria-label="Laptop showing a campaign image"></div>
  <div class="cap" style="left:80px;top:106px;width:110px;text-align:left"><b>Full Sale in Greenwich</b>Mostly recent work cases included from the team and partners across our markets.</div>
  <div class="footer"><div class="cubes"></div><span class="copy">© 2013 Velmoxa. All rights reserved</span><span class="num">8</span></div>
</section>

<section class="slide c3 r3">
  <div class="brand"><i></i>Velmoxa</div>
  <div class="map-area" role="img" aria-label="Blue world map with regional percentage labels and small grey people counts"></div>
  <div class="footer"><div class="cubes"></div><span class="copy">© 2013 Velmoxa. All rights reserved</span><span class="num">9</span></div>
</section>

<section class="slide hero divider c1 r4">
  <div class="brand-lg"><i></i>Velmoxa</div>
  <div class="band"></div>
  <div class="big">DIVIDER PAGES HERE</div>
  <div class="sub" style="top:96px">YOUR SECTION SUB TITLE HERE</div>
  <div class="strip" role="img" aria-label="Bright multicoloured cubes"></div>
  <span class="fcopy">© 2013 Velmoxa. All rights reserved</span>
</section>

<section class="slide c2 r4">
  <h2 class="title">VELMOXA PRESENTATION POWERFUL MISSION 1</h2>
  <div class="brand"><i></i>Velmoxa</div>
  <svg style="position:absolute;left:38px;top:40px" width="180" height="32" viewBox="0 0 180 32">
    <g font-family="Open Sans,sans-serif" font-size="3.6" font-weight="700" fill="#fff" text-anchor="middle">
      <circle cx="16" cy="16" r="15" fill="#1b4f8f"/><text x="16" y="17.5">BRIEF</text>
      <circle cx="53" cy="16" r="15" fill="#2466a8"/><text x="53" y="17.5">ANALIZE</text>
      <circle cx="90" cy="16" r="15" fill="#2d8fd2"/><text x="90" y="17.5">DESIGN</text>
      <circle cx="127" cy="16" r="15" fill="#4fa8de"/><text x="127" y="17.5">DEVELOP</text>
      <circle cx="164" cy="16" r="15" fill="#7cc1e8"/><text x="164" y="17.5">TESTING</text>
    </g>
  </svg>
  <div style="position:absolute;left:24px;top:84px;width:208px">
    <p class="body">The agency has forged a courageous and dynamic approach to the methods of brand research. The pace of work followed from each stage of the process, overcoming old habits that held the field back and raising strategy to a new level.</p>
    <p class="body">By overcoming old habits that held the field back, the team has raised the level of strategy to a new standard and brings fresh ideas to every client.</p>
  </div>
  <div class="footer"><div class="cubes"></div><span class="copy">© 2013 Velmoxa. All rights reserved</span><span class="num">11</span></div>
</section>

<section class="slide c3 r4">
  <div class="brand"><i></i>Velmoxa</div>
  <svg style="position:absolute;left:30px;top:30px" width="90" height="100" viewBox="0 0 90 100">
    <g font-family="Open Sans,sans-serif" font-size="3.6" font-weight="700" fill="#fff" text-anchor="middle">
      <circle cx="45" cy="52" r="44" fill="#b9bec4"/><text x="45" y="16">BRIEF</text>
      <circle cx="45" cy="60" r="35" fill="#8f969e"/><text x="45" y="31">ANALIZE</text>
      <circle cx="45" cy="67" r="27" fill="#5ab2e4"/><text x="45" y="46">DESIGN</text>
      <circle cx="45" cy="73" r="20" fill="#2d8fd2"/><text x="45" y="59">DEVELOP</text>
      <circle cx="45" cy="78" r="14" fill="#1b6aa8"/><text x="45" y="80">TESTING</text>
    </g>
  </svg>
  <ul class="bullets" style="left:140px;top:40px">
    <li>Since 1990, we have supported</li><li>Essential to this approach in review</li><li>Habits that held the field back</li><li>Since 1990, we have supported</li><li>Essential to this approach in review</li><li>Habits that held the field back</li><li>Text has propelled the leader</li><li>Multiple new research tools</li><li>Since 1990, we have supported</li><li>Essential to this approach in review</li><li>Habits that held the field back</li>
  </ul>
  <div class="footer"><div class="cubes"></div><span class="copy">© 2013 Velmoxa. All rights reserved</span><span class="num">12</span></div>
</section>

<section class="slide c1 r5">
  <h2 class="title">VELMOXA PRESENTATION POWERFUL MISSION 1</h2>
  <div class="brand"><i></i>Velmoxa</div>
  <div style="position:absolute;left:22px;top:42px;width:92px">
    <p class="body">The agency has forged a courageous and dynamic approach to the methods of brand research. By overcoming old habits, the team raised the level of strategy.</p>
    <p class="body">Central to this approach are focused audits that hold the work together. The team has raised the bar of multiple projects and keeps the spirit of change in every task for each client.</p>
  </div>
  <svg style="position:absolute;left:128px;top:52px" width="100" height="64" viewBox="0 0 100 64">
    <ellipse cx="50" cy="36" rx="46" ry="24" fill="#1b6aa8"/>
    <ellipse cx="50" cy="30" rx="46" ry="24" fill="#2d8fd2"/>
    <path d="M50 30 L50 6 A46 24 0 0 0 6 26 Z" fill="#8f969e"/>
    <path d="M50 30 L6 26 A46 24 0 0 0 22 49 Z" fill="#c3c8cd"/>
  </svg>
  <div class="legend" style="left:130px;top:124px"><span>Product</span><span>Product</span><span>Product</span><span>Product</span></div>
  <div class="footer"><div class="cubes"></div><span class="copy">© 2013 Velmoxa. All rights reserved</span><span class="num">13</span></div>
</section>

<section class="slide c2 r5">
  <h2 class="title">VELMOXA PRESENTATION POWERFUL MISSION 1</h2>
  <div class="brand"><i></i>Velmoxa</div>
  <div style="position:absolute;left:22px;top:42px;width:96px">
    <p class="body">The agency has forged a courageous and dynamic approach to the methods of brand research. By overcoming old habits, the team raised the level of strategy.</p>
    <p class="body">Central to this approach are focused audits that hold the work together. The team has raised the bar of multiple projects and keeps the spirit of change in every task for each client.</p>
  </div>
  <svg style="position:absolute;left:140px;top:46px" width="90" height="80" viewBox="0 0 90 80">
    <rect x="4" y="56" width="14" height="20" fill="#b9bec4"/><polygon points="18,56 22,53 22,73 18,76" fill="#8f969e"/><polygon points="4,56 8,53 22,53 18,56" fill="#d5d9dd"/>
    <rect x="26" y="44" width="14" height="32" fill="#8f969e"/><polygon points="40,44 44,41 44,73 40,76" fill="#6b737c"/><polygon points="26,44 30,41 44,41 40,44" fill="#b9bec4"/>
    <rect x="48" y="28" width="14" height="48" fill="#5ab2e4"/><polygon points="62,28 66,25 66,73 62,76" fill="#2d8fd2"/><polygon points="48,28 52,25 66,25 62,28" fill="#9fd3f0"/>
    <rect x="70" y="8" width="14" height="68" fill="#2d8fd2"/><polygon points="84,8 88,5 88,73 84,76" fill="#1b6aa8"/><polygon points="70,8 74,5 88,5 84,8" fill="#6cc0ea"/>
  </svg>
  <div class="legend" style="left:136px;top:130px"><span>Product</span><span>Product</span><span>Product</span><span>Product</span></div>
  <div class="footer"><div class="cubes"></div><span class="copy">© 2013 Velmoxa. All rights reserved</span><span class="num">14</span></div>
</section>

<section class="slide c3 r5">
  <h2 class="title">VELMOXA PRESENTATION POWERFUL MISSION 1</h2>
  <div class="brand"><i></i>Velmoxa</div>
  <div style="position:absolute;left:20px;top:44px;width:92px">
    <p class="body">The agency has forged a courageous and dynamic approach to the methods of brand research. By overcoming old habits, the team raised the level of strategy.</p>
    <p class="body">Central to this approach are focused audits that hold the work together. The team has raised the bar of multiple projects and keeps the spirit of change in every task.</p>
  </div>
  <table class="data" style="left:122px;top:44px;width:118px">
    <tr><th>No</th><th>Name</th><th>Date</th><th>Case</th></tr>
    <tr><td>01</td><td>Ola Brenner</td><td>17-06-13</td><td>Open</td></tr>
    <tr><td>02</td><td>Ivo Karsten</td><td>17-06-13</td><td>Open</td></tr>
    <tr><td>03</td><td>Ola Brenner</td><td>17-06-13</td><td>Close</td></tr>
    <tr><td>04</td><td>Ivo Karsten</td><td>17-06-13</td><td>Open</td></tr>
    <tr><td>05</td><td>Ola Brenner</td><td>17-06-13</td><td>Open</td></tr>
    <tr><td>06</td><td>Ivo Karsten</td><td>17-06-13</td><td>Close</td></tr>
    <tr><td>07</td><td>Ola Brenner</td><td>17-06-13</td><td>Open</td></tr>
    <tr><td>08</td><td>Ivo Karsten</td><td>17-06-13</td><td>Open</td></tr>
  </table>
  <div class="footer"><div class="cubes"></div><span class="copy">© 2013 Velmoxa. All rights reserved</span><span class="num">15</span></div>
</section>

<section class="slide c1 r6">
  <h2 class="title">VELMOXA PRESENTATION POWERFUL MISSION 1</h2>
  <div class="brand"><i></i>Velmoxa</div>
  <table class="data" style="left:24px;top:40px;width:208px">
    <tr><th>No</th><th>Name</th><th>Id Line</th><th>Address</th><th>Date</th><th>Case</th></tr>
    <tr><td>01</td><td>Ola Brenner</td><td>421896</td><td>Hall Street 24a</td><td>17-06-13</td><td>Open</td></tr>
    <tr><td>02</td><td>Ivo Karsten</td><td>421896</td><td>Alder Street 14a</td><td>17-06-13</td><td>Open</td></tr>
    <tr><td>03</td><td>Ola Brenner</td><td>421896</td><td>Village Street 14a</td><td>17-06-13</td><td>Close</td></tr>
    <tr><td>04</td><td>Ivo Karsten</td><td>421896</td><td>Bridge Street 14a</td><td>17-06-13</td><td>Open</td></tr>
    <tr><td>05</td><td>Ola Brenner</td><td>421896</td><td>Hall Street 24a</td><td>17-06-13</td><td>Open</td></tr>
  </table>
  <div style="position:absolute;left:24px;top:110px;width:208px">
    <p class="body">The agency has forged a courageous and dynamic approach to the methods of brand research. By overcoming old habits that held the field back, the team has raised the level of strategy to a new standard.</p>
    <p class="body">Central to this approach are focused audits that hold the work together, raising the bar of projects.</p>
  </div>
  <div class="footer"><div class="cubes"></div><span class="copy">© 2013 Velmoxa. All rights reserved</span><span class="num">16</span></div>
</section>

<section class="slide c2 r6">
  <h2 class="title">VELMOXA PRESENTATION POWERFUL MISSION 1</h2>
  <div class="brand"><i></i>Velmoxa</div>
  <table class="data" style="left:24px;top:40px;width:208px">
    <tr><th>No</th><th>Name</th><th>Id Line</th><th>Address</th><th>Date</th><th>Case</th></tr>
    <tr><td>01</td><td>Ola Brenner</td><td>421896</td><td>Hall Street 24a</td><td>17-06-13</td><td>Open</td></tr>
    <tr><td>02</td><td>Ivo Karsten</td><td>421896</td><td>Alder Street 14a</td><td>17-06-13</td><td>Open</td></tr>
    <tr><td>03</td><td>Ola Brenner</td><td>421896</td><td>Village Street 14a</td><td>17-06-13</td><td>Close</td></tr>
    <tr><td>04</td><td>Ivo Karsten</td><td>421896</td><td>Bridge Street 14a</td><td>17-06-13</td><td>Open</td></tr>
    <tr><td>05</td><td>Ola Brenner</td><td>421896</td><td>Hall Street 24a</td><td>17-06-13</td><td>Open</td></tr>
  </table>
  <div style="position:absolute;left:24px;top:110px;width:208px">
    <p class="body">The agency has forged a courageous and dynamic approach to the methods of brand research. By overcoming old habits that held the field back, the team has raised the level of strategy to a new standard.</p>
    <p class="body">Central to this approach are focused audits that hold the work together, raising the bar of projects.</p>
  </div>
  <div class="footer"><div class="cubes"></div><span class="copy">© 2013 Velmoxa. All rights reserved</span><span class="num">17</span></div>
</section>

<section class="slide hero closing c3 r6">
  <div class="brand-lg"><i></i>Velmoxa</div>
  <div class="band"></div>
  <div class="strip" role="img" aria-label="Soft blue city skyline backdrop"></div>
  <div class="big" style="top:92px">THANK YOU</div>
  <div class="sub" style="top:111px">FOR YOUR ATTENTION</div>
  <span class="copy" style="left:auto;right:10px;bottom:6px">© 2013 Velmoxa. All rights reserved</span>
</section>

</main>
</body>
</html>
```